smile partners of lakeview | ||
business cards/stationary | ||
Cutting-Edge Professional |
Dr. Marcus Holloway / Dr. Leonardo Brisco | ||
President | ||
Bayonne 57 Ave K Bayonne, NJ 07002 201-555-0142 ********* East Orange 42 North Whitfield St Suite 208 East Orange, NJ 07018 973-555-0187 ******** North Bergen 4829 Larkmoor North Bergen, NJ 07047 201-555-0163 ********** Union City 2748 Quenton Ave Union City, NJ 07087 201-555-0129 ********* Paterson 3170 Elm street Suite K Paterson, NJ 07503 973 555-0114 ******** |
office@quentondental.example | ||
www.SmilePartnersOfLV.example | ||
We need 7 different business card designs. 1. Dr Marcus Holloway (no address..just website) 2. Dr Leonardo Brisco (no address just website) 3. Smile Partners of Lakeview - East Orange 4. Smile Partners of Lakeview - Bayone 5. Smile Partners of Lakeview- Union City 6. Smile Partners of Lakeview- North Bergen 7. Smile Partners of Lakeview- Paterson Business Cards 3-7 do not need to include Dr Holloway/Dr Brisco's name on them |
For the personal cards (Dr Marcus Holloway and Dr Leo Brisco) use the back of the cards to tell all of the office locations For the Office cards (3-7) use the back of the card for appointments...we will upload a sample background that we currently use. |
554611_1195_4351.png |
photo3_JPG4352.jpg |
DentalGroups_Paterson_4421.pdf |
DentalGroups_Paterson_4422.gif |
DentalGroups_Paterson_4423.eps |
DentalGroups_Web_4424.png |
DentalGroups_Web_4425.ai |
DentalGroups_Web_4426.gif |

```html
<!DOCTYPE html>
<html lang="en">
<head>
<meta charset="utf-8">
<title>Smile Partners of Lakeview – Paterson Office Card</title>
<link rel="stylesheet" href="https://fonts.googleapis.com/css2?family=Tinos:wght@400&display=swap">
<style>
  :root {
    --brown: #6b3d14;
    --gold: #c99a3a;
    --gold-light: #e6c47a;
    --ink: #2a2a2a;
    --muted: #444444;
    --paper: #ffffff;
    --frame: #9a9a9a;
    --canvas: #ffffff;
  }
  * { box-sizing: border-box; margin: 0; padding: 0; }
  html, body { width: 1200px; height: 338px; overflow: hidden; background: var(--canvas); }
  .sheet { position: relative; width: 1200px; height: 338px; font-family: "Tinos", "Times New Roman", serif; }

  .card {
    position: absolute; top: 0; height: 338px; background: var(--paper);
    border: 1px solid var(--frame); overflow: hidden;
  }
  .card--front { left: 0; width: 581px; }
  .card--back { left: 602px; width: 598px; color: var(--ink); }

  .front__swoosh { position: absolute; top: 0; left: 0; width: 581px; height: 110px; }

  .brand {
    position: absolute; left: 22px; top: 236px; display: flex; align-items: center; gap: 12px;
  }
  .brand__dot { width: 18px; height: 18px; border-radius: 50%; background: var(--gold); flex: none; }
  .brand__name {
    color: var(--brown); font-size: 30px; font-weight: 400; line-height: 1.05; width: 250px;
  }

  .contact { position: absolute; left: 358px; top: 186px; font-size: 12px; color: var(--muted); line-height: 1.35; }
  .contact__address { margin-bottom: 16px; }

  .appt__title { text-align: center; font-size: 31px; font-weight: 400; margin-top: 20px; }
  .appt__line { position: absolute; left: 24px; right: 24px; display: flex; align-items: flex-end; font-size: 16px; border-bottom: 1px solid var(--ink); padding-bottom: 3px; }
  .appt__line--for { top: 74px; }
  .appt__line--date { top: 220px; }
  .appt__line--date span:last-child { margin-left: 218px; }

  .days { position: absolute; left: 24px; top: 156px; display: flex; gap: 18px; font-size: 16px; }
  .day { display: flex; align-items: center; gap: 6px; }
  .day__box { width: 22px; height: 22px; border: 1.5px solid var(--ink); }

  .appt__note { position: absolute; left: 0; right: 0; top: 294px; text-align: center; font-size: 15px; }
</style>
</head>
<body>
<main class="sheet">
  <section class="card card--front" aria-label="Paterson office card front">
    <svg class="front__swoosh" viewBox="0 0 581 110" preserveAspectRatio="none" aria-hidden="true">
      <path d="M0 0 H581 V34 C430 22 300 40 180 70 C110 88 50 98 0 100 Z" fill="var(--gold)"/>
      <path d="M0 0 H581 V26 C430 14 300 30 180 58 C110 76 50 86 0 90 Z" fill="var(--brown)"/>
      <path d="M0 92 C60 90 120 80 180 66 C300 36 430 20 581 30" fill="none" stroke="var(--gold-light)" stroke-width="2"/>
    </svg>

    <div class="brand">
      <span class="brand__dot"></span>
      <span class="brand__name">Smile Partners of Lakeview</span>
    </div>

    <div class="contact">
      <p class="contact__address">3170 Elm street<br>Suite K<br>Paterson, NJ 07503<br>973 555-0114</p>
      <p>Email : office@quentondental.example</p>
      <p>Web : www.SmilePartnersOfLV.example</p>
    </div>
  </section>

  <section class="card card--back" aria-label="Appointment card back">
    <h1 class="appt__title">Appointment</h1>
    <div class="appt__line appt__line--for"><span>For</span></div>
    <div class="days">
      <span class="day"><span class="day__box"></span>Mon</span>
      <span class="day"><span class="day__box"></span>Tue</span>
      <span class="day"><span class="day__box"></span>Wed</span>
      <span class="day"><span class="day__box"></span>Thr</span>
      <span class="day"><span class="day__box"></span>Fri</span>
      <span class="day"><span class="day__box"></span>Sat</span>
      <span class="day"><span class="day__box"></span>Sun</span>
    </div>
    <div class="appt__line appt__line--date"><span>Date</span><span>Time</span></div>
    <p class="appt__note">If You Are Unable to keep this Appointment, Please Notice use for 24 hours</p>
  </section>
</main>
</body>
</html>
```